New Business Card Design Project

I would like my card design to look exactly like the logo, design, layout, and print of the current attached file. The only change I would like made would be for the print to say THE KMW GROUP instead of THE HALLORAN GROUP. Basically, just replace his group name with my group name. I would also like the backgroud to be the same texture and color as the attached file. I love the dark blue lettering and house logo on the card.

I am completely open to the rest of the card design. I just want something clean and simple. Only basic contact info required on the card. Maybe just name: Kyle M Warrick and cell # 555.914.2087 and email kyle@orchidhomesagent.com

```html
<!DOCTYPE html>
<html lang="en">
<head>
<meta charset="utf-8">
<title>The KMW Group – Business Card</title>
<link rel="stylesheet" href="https://fonts.googleapis.com/css2?family=Arimo:wght@700&family=Montserrat:wght@400&family=Open+Sans:wght@400&display=swap">
<style>
  :root {
    --backdrop: #1b1b1d;
    --silver-light: #ececec;
    --silver-mid: #d4d4d4;
    --silver-dark: #bdbdbd;
    --navy: #141a3c;
    --navy-card: #10132f;
    --ink-white: #ffffff;
    --rule: #8f93a8;
  }
  * { margin: 0; padding: 0; box-sizing: border-box; }
  html, body {
    width: 1200px;
    height: 900px;
    overflow: hidden;
    background: var(--backdrop);
  }
  .stage {
    width: 1200px;
    height: 900px;
    display: flex;
    flex-direction: column;
    align-items: center;
    justify-content: center;
    gap: 48px;
  }
  .card {
    width: 560px;
    height: 320px;
    border-radius: 22px;
    position: relative;
    box-shadow: 0 14px 30px rgba(0, 0, 0, 0.55);
  }
  .card--front {
    background: linear-gradient(135deg, var(--silver-light) 0%, var(--silver-mid) 45%, var(--silver-dark) 75%, var(--silver-mid) 100%);
    display: flex;
    align-items: center;
    justify-content: center;
  }
  .brand {
    display: flex;
    align-items: center;
    gap: 26px;
  }
  .brand__square {
    width: 78px;
    height: 78px;
    background: var(--navy);
  }
  .brand__name {
    font-family: "Montserrat", sans-serif;
    font-weight: 400;
    color: var(--navy);
    font-size: 26px;
    line-height: 1.08;
    letter-spacing: 0.22em;
  }
  .brand__name span { display: block; }
  .card--back {
    background: var(--navy-card);
    display: flex;
    flex-direction: column;
    align-items: center;
    justify-content: center;
    color: var(--ink-white);
  }
  .contact__name {
    font-family: "Arimo", sans-serif;
    font-weight: 700;
    font-size: 33px;
    letter-spacing: 0.02em;
  }
  .contact__rule {
    width: 230px;
    height: 1px;
    background: var(--rule);
    margin: 14px 0 12px;
  }
  .contact__line {
    font-family: "Open Sans", sans-serif;
    font-size: 23px;
    line-height: 1.3;
    letter-spacing: 0.01em;
  }
</style>
</head>
<body>
  <main class="stage">
    <section class="card card--front" aria-label="Card front">
      <div class="brand">
        <div class="brand__square" aria-hidden="true"></div>
        <p class="brand__name"><span>THE</span><span>KMW</span><span>GROUP</span></p>
      </div>
    </section>
    <section class="card card--back" aria-label="Card back">
      <h1 class="contact__name">KYLE M WARRICK</h1>
      <div class="contact__rule"></div>
      <p class="contact__line">555.914.2087</p>
      <p class="contact__line">kyle@orchidhomesagent.com</p>
    </section>
  </main>
</body>
</html>
```